Eneginering consultancy brochure style web design project

Looking for a new brochure style web page for our small engineering consultancy. The prupose of the website is to provide some basic information with about the company, including exampels of our work, and present a way to initiate contact. There there will only be a few pages (up to 5) and limited content.A main focus of the project is to develop the visual design/identity for the webpage, and to provide the template for us to add content, rearrange layout and modify pages with relative ease.A mixture of text and images will be used. The use of an image slider would be desirable.We have recently had a new company logo developed (uploaded), which defines the colour scheme for the page.A professional. clean look is desired, that is not cluttered and easy to navigate.Template to add a photo slider is desirable.The use of swirl patterns (suach as those used here: https://www.brightvortexlab.co.uk/) and/or contoured mesh pattern (example attached) within the page is likely to be attractive, as this is in harmony with our activities.

Target Market(s)

Engineering; manufacturing

Industry/Entity Type

Engineering Consultant

Coding

Coded - Design and coding required

Number of Pages Required

3 page

Font styles to use
Other font styles liked:
• Helvetica

Colors
00a990
33b8a4
86cfc6
606060
3176b5
0255a3
85acd3
474747
7f7f7f

Requirements
Must have
• 1) Landing page for information about the company. Mostly text, with image slider.
• 2) One page for example projects. Images with accompanying texts.
• 3) Enquiry/'get in touch' page.
• Simple, uncluttered look and feel.

```html
<!DOCTYPE html>
<html lang="en">
<head>
<meta charset="utf-8">
<title>Thermaflow Engineering</title>
<link rel="stylesheet" href="https://fonts.googleapis.com/css2?family=Montserrat:wght@400;500;600;700&display=swap">
<style>
:root{
  --blue:#1f74bd;
  --blue-dark:#0255a3;
  --blue-soft:#85acd3;
  --teal:#33b8a4;
  --teal-dark:#00a990;
  --grey:#606060;
  --grey-dark:#474747;
  --grey-mid:#7f7f7f;
  --text:#4a4a4a;
  --white:#ffffff;
  --page:#f4f5f6;
}
*{margin:0;padding:0;box-sizing:border-box}
html,body{width:1200px;height:3125px;overflow:hidden}
body{font-family:"Montserrat",Helvetica,Arial,sans-serif;color:var(--text);background:var(--white);position:relative}
.block{position:absolute;left:0;width:1200px}

/* header */
.site-header{top:0;height:90px;background:var(--white)}
.brand{position:absolute;left:100px;top:14px;display:flex;align-items:center;gap:10px}
.brand-dot{width:22px;height:22px;border-radius:50%;background:var(--blue)}
.brand-name{font-size:26px;font-weight:700;color:var(--blue);letter-spacing:1px}
.socials{position:absolute;left:122px;top:66px;display:flex;gap:6px}
.socials span{width:16px;height:16px;border-radius:50%;background:var(--blue)}
.header-phone{position:absolute;right:90px;top:18px;font-size:11px;color:var(--grey);display:flex;align-items:center;gap:6px}
.main-nav{position:absolute;right:82px;top:60px;display:flex;gap:0}
.main-nav a{font-size:12px;color:var(--grey);text-decoration:none;padding:4px 18px 12px;position:relative}
.main-nav a.active::after{content:"";position:absolute;left:0;right:0;bottom:-1px;height:4px;background:var(--blue)}

/* hero */
.hero{top:90px;height:415px;background:#8a4a2c}
.hero-photo{position:absolute;top:0;height:415px}
.hero-photo.left{left:0;width:358px;background:linear-gradient(135deg,#5a2c18,#c27a52 45%,#7a3d22 70%,#d89670)}
.hero-photo.right{left:848px;width:352px;background:linear-gradient(60deg,#6b3420,#c98259 40%,#8c4a2c 65%,#e2a47c)}
.hero-panel{position:absolute;left:358px;width:490px;top:0;height:415px;background:linear-gradient(160deg,#2d6db0,#3c84c6 55%,#2a63a2);text-align:center;color:var(--white)}
.hero-mark{width:50px;height:4px;background:var(--white);margin:120px auto 24px;border-radius:2px}
.hero-panel h1{font-size:22px;font-weight:700;line-height:1.35;padding:0 26px;text-transform:uppercase}
.hero-panel p{font-size:11.5px;line-height:1.55;padding:18px 28px 0}
.slider-dots{position:absolute;left:0;right:0;top:375px;display:flex;justify-content:center;gap:13px}
.slider-dots span{width:15px;height:15px;border-radius:50%;background:rgba(255,255,255,.6)}
.slider-dots span.on{background:var(--white)}

/* section titles */
.section-title{position:absolute;left:88px;display:flex;align-items:center;gap:14px;font-size:19px;font-weight:700;text-transform:uppercase;color:var(--grey-dark)}
.section-title .mark{width:34px;height:4px;border-radius:2px;background:var(--blue)}
.section-title.light{color:var(--white)}
.section-title.light .mark{background:var(--white)}

/* services */
.services{top:505px;height:510px;background:linear-gradient(180deg,#ffffff 0%,#f2f3f4 60%,#e9eaec 100%)}
.services .section-title{top:76px}
.intro{position:absolute;left:88px;font-size:12px;color:var(--text)}
.services .intro{top:130px}
.service-list{position:absolute;top:184px;left:88px;display:flex;gap:21px}
.service{width:240px;height:240px;border-radius:50%;background:var(--blue);color:var(--white);text-align:center;display:flex;flex-direction:column;align-items:center;padding-top:40px}
.service svg{width:100px;height:100px}
.service p{font-size:12px;line-height:1.45;margin-top:28px;padding:0 30px}

/* software */
.software{top:1015px;height:440px;background:linear-gradient(90deg,#ffffff,#f3f4f5 60%,#ececee)}
.software .section-title{top:52px}
.copy{position:absolute;left:88px;width:510px;font-size:12px;line-height:1.5}
.copy p{margin-bottom:15px}
.software .copy{top:120px}
.tool-board{position:absolute;left:666px;top:0;width:446px;height:385px;background:var(--white);display:grid;grid-template-columns:1fr 1fr;gap:22px;padding:22px}
.tool-badge{border-radius:6px;background:#e6eaef}

/* about */
.wave{position:absolute;left:0;top:1420px;width:1200px;height:130px}
.about{top:1540px;height:632px;background:var(--blue)}
.about .section-title{top:48px}
.about-logo{position:absolute;left:170px;top:118px;display:flex;align-items:center;gap:14px}
.about-logo .brand-dot{width:34px;height:34px;background:var(--white)}
.about-logo .brand-name{font-size:44px;color:var(--white)}
.about .copy{top:262px;color:var(--white);width:500px}
.profile{position:absolute;left:803px;top:130px;width:280px;text-align:center;color:var(--white)}
.profile-photo{width:280px;height:280px;border-radius:50%;background:radial-gradient(circle at 50% 45%,#7d8a70,#4f6a3c 55%,#2f3d2a);border:4px solid var(--white)}
.profile-badge{width:46px;height:46px;border-radius:50%;background:var(--teal);margin:-24px auto 0;position:relative}
.profile-name{font-size:19px;font-weight:700;margin-top:10px}
.profile-role{font-size:12px;margin-top:4px}

/* contact */
.contact{top:2172px;height:653px;background:linear-gradient(90deg,#ffffff 0%,#f6f6f6 55%,#e9e9e9 100%)}
.contact .section-title{top:74px}
.contact .intro{top:124px;width:490px;line-height:1.55}
.contact-list{position:absolute;left:88px;top:230px;list-style:none;font-size:14px;color:var(--grey-dark)}
.contact-list li{display:flex;gap:22px;align-items:flex-start;margin-bottom:28px;line-height:1.4}
.contact-list svg{width:32px;height:32px;flex:none}
.contact-photo{position:absolute;left:720px;top:36px;width:480px;height:617px;background:linear-gradient(200deg,#5a3a2a,#b08270 35%,#e2d6d0 60%,#3a3a44)}

/* footer */
.site-footer{top:2825px;height:300px;background:var(--grey);color:var(--white);text-align:center}
.footer-nav{margin-top:60px;font-size:14px}
.footer-brand{display:inline-flex;align-items:center;gap:10px;margin-top:28px}
.footer-brand .brand-dot{background:var(--white);width:26px;height:26px}
.footer-brand .brand-name{color:var(--white);font-size:32px}
.copyright{font-size:11px;margin-top:28px;line-height:1.6}
</style>
</head>
<body>

<header class="block site-header">
  <div class="brand"><span class="brand-dot"></span><span class="brand-name">TFE</span></div>
  <div class="socials"><span></span><span></span><span></span><span></span></div>
  <div class="header-phone">
    <svg width="12" height="12" viewBox="0 0 24 24"><path fill="#606060" d="M6.6 10.8a15 15 0 0 0 6.6 6.6l2.2-2.2c.3-.3.7-.4 1-.2 1.1.4 2.3.6 3.6.6.6 0 1 .4 1 1V20c0 .6-.4 1-1 1A17 17 0 0 1 3 4c0-.6.4-1 1-1h3.5c.6 0 1 .4 1 1 0 1.3.2 2.5.6 3.6.1.3 0 .7-.2 1z"/></svg>
    +44 (0)7700 900 418
  </div>
  <nav class="main-nav"><a class="active" href="#">Home</a><a href="#">About</a><a href="#">Services</a><a href="#">Contact</a></nav>
</header>

<section class="block hero">
  <div class="hero-photo left" role="img" aria-label="Close-up of copper motor windings"></div>
  <div class="hero-panel">
    <div class="hero-mark"></div>
    <h1>Thermal design, simulations and analysis of electrical machines</h1>
    <p>TFE offers thermal analysis and design for electrical machine design projects. We use a range of both commercial and in-house software for the design and optimisation of electrical machines using a multi-physics approach.</p>
  </div>
  <div class="hero-photo right" role="img" aria-label="Copper coil windings of an electrical machine"></div>
  <div class="slider-dots"><span class="on"></span><span></span><span></span><span></span><span></span></div>
</section>

<section class="block services">
  <h2 class="section-title"><span class="mark"></span>Services</h2>
  <p class="intro">TFE can assist through all stages of your project:</p>
  <div class="service-list">
    <div class="service">
      <svg viewBox="0 0 100 100" fill="none" stroke="#fff" stroke-width="4" stroke-linecap="round"><path d="M38 70c0-10-12-16-12-30a24 24 0 0 1 48 0c0 14-12 20-12 30z"/><path d="M40 78h20M42 86h16"/><path d="M50 4v8M14 20l6 5M86 20l-6 5M6 44h8M86 44h8"/></svg>
      <p>Experience and intuition for concept generation</p>
    </div>
    <div class="service">
      <svg viewBox="0 0 100 100"><path fill="#fff" d="M50 8l38 18v46L50 92 12 72V26z"/><path fill="none" stroke="#1f74bd" stroke-width="4" d="M12 26l38 18 38-18M50 44v48"/></svg>
      <p>Thermo-fluid modelling and simulation for design</p>
    </div>
    <div class="service">
      <svg viewBox="0 0 100 100" fill="none" stroke="#fff" stroke-width="4" stroke-linecap="round"><path d="M42 62V14a8 8 0 0 1 16 0v48a15 15 0 1 1-16 0z"/><circle cx="50" cy="74" r="7" fill="#fff"/><path d="M50 70V36M66 24h10M66 34h10M66 44h10"/></svg>
      <p>Application of a range of thermal simulation tools</p>
    </div>
    <div class="service">
      <svg viewBox="0 0 100 100" fill="none" stroke="#fff" stroke-width="4" stroke-linecap="round" stroke-linejoin="round"><path d="M22 6h40l18 18v70H22z"/><path d="M62 6v18h18"/><path d="M32 42l4 4 8-8M52 42h18M32 62l4 4 8-8M52 62h18M34 78h10M52 80h18"/></svg>
      <p>Test data acquisition for design validation and optimisation</p>
    </div>
  </div>
</section>

<section class="block software">
  <h2 class="section-title"><span class="mark"></span>Softwares</h2>
  <div class="copy">
    <p>We are experienced with many different software packages, enabling us to select the most appropriate tools for each project. This includes CFD, thermal resistance modelling, analytical sizing tools and multi-objective optimisation tools.</p>
    <p>We also develop bespoke thermal analysis tools for novel machine types and applications which are beyond the limitations of commercial packages. These parameterised analysis tools can be used by us to design and optimise your design. Designed with user-friendliness in mind, they can also be designed for use by you and your design teams.</p>
    <p>We offer a professional approach to all work, using our experience to provide industry standard deliverables on the timescales agreed.</p>
  </div>
  <div class="tool-board">
    <div class="tool-badge"></div><div class="tool-badge"></div>
    <div class="tool-badge"></div><div class="tool-badge"></div>
  </div>
</section>

<svg class="wave" viewBox="0 0 1200 130" preserveAspectRatio="none">
  <path fill="#33b8a4" d="M0 60C220 0 420 20 640 50S1020 40 1200 0V130H0z"/>
  <path fill="#1f74bd" d="M0 110C260 60 480 70 700 95S1040 80 1200 60V130H0z"/>
</svg>

<section class="block about">
  <h2 class="section-title light"><span class="mark"></span>About TFE</h2>
  <div class="about-logo"><span class="brand-dot"></span><span class="brand-name">TFE</span></div>
  <div class="copy">
    <p>We are experienced with many different software packages, enabling us to select the most appropriate tools for each project. This includes CFD, thermal resistance modelling, analytical sizing tools and multi-objective optimisation tools.</p>
    <p>We also develop bespoke thermal analysis tools for novel machine types and applications which are beyond the limitations of commercial packages. These parameterised analysis tools can be used by us to design and optimise your design. Designed with user-friendliness in mind, they can also be designed for use by you and your design teams.</p>
    <p>We offer a professional approach to all work, using our experience to provide industry standard deliverables on the timescales agreed.</p>
  </div>
  <div class="profile">
    <div class="profile-photo" role="img" aria-label="Portrait of the managing director outdoors"></div>
    <div class="profile-badge"></div>
    <div class="profile-name">Daniel Harwood</div>
    <div class="profile-role">Managing Director</div>
  </div>
</section>

<section class="block contact">
  <h2 class="section-title"><span class="mark"></span>Contact us</h2>
  <p class="intro">To get in contact with Thermaflow Engineering, please use one of the contact methods below.</p>
  <ul class="contact-list">
    <li><svg viewBox="0 0 32 32"><rect x="1" y="6" width="30" height="20" rx="2" fill="#474747"/><path d="M2 8l14 10 14-10" fill="none" stroke="#fff" stroke-width="2"/></svg>enquiries@thermaflowengineering.com</li>
    <li><svg viewBox="0 0 24 24"><path fill="#474747" d="M6.6 10.8a15 15 0 0 0 6.6 6.6l2.2-2.2c.3-.3.7-.4 1-.2 1.1.4 2.3.6 3.6.6.6 0 1 .4 1 1V20c0 .6-.4 1-1 1A17 17 0 0 1 3 4c0-.6.4-1 1-1h3.5c.6 0 1 .4 1 1 0 1.3.2 2.5.6 3.6.1.3 0 .7-.2 1z"/></svg>+44 (0)7700 900 418</li>
    <li><svg viewBox="0 0 24 24"><path fill="#474747" d="M12 1a8 8 0 0 0-8 8c0 6 8 14 8 14s8-8 8-14a8 8 0 0 0-8-8zm0 11a3 3 0 1 1 0-6 3 3 0 0 1 0 6z"/></svg>
      <span>Thermaflow Engineering Ltd<br>Unit 4 Meridian Court<br>Riverside Science Park<br>Foundry Lane<br>Lenton<br>NG9 4XQ</span></li>
  </ul>
  <div class="contact-photo" role="img" aria-label="Smiling customer support agent wearing a headset"></div>
</section>

<footer class="block site-footer">
  <div class="footer-nav">Home | Service | About | Contact | Back to Top</div>
  <div class="footer-brand"><span class="brand-dot"></span><span class="brand-name">TFE</span></div>
  <div class="copyright">COPYRIGHT © 2019, ALL RIGHTS RESERVED.<br>Terms and Conditions | Privacy Policy</div>
</footer>

</body>
</html>
```